Varrow Property Group Business cards

I am starting a property development and consultancy business called Varrow Property Group. I have a logo designed and a website on its way:
www.varrowgroup-example.com.au

I need a business card with the following:

Front:
Mostly orange with logo taking up all front of card

Back of card:
Logo

Miles Harcourt
Managing Director

T +61 455 207 364
E miles.harcourt@varrowgroup-example.com.au
www.varrowgroup-example.com.au

Industry/Entity Type

Business

Requirements
Must have
• curved edges

```html
<!DOCTYPE html>
<html lang="en">
<head>
<meta charset="utf-8">
<title>Varrow Property Group – Business Cards</title>
<link rel="stylesheet" href="https://fonts.googleapis.com/css2?family=Archivo+Narrow:wght@400;600;700&display=swap">
<style>
  :root {
    --bg: #2b2b2b;
    --orange: #f5a31a;
    --orange-soft: #f9c468;
    --white: #ffffff;
    --paper: #f7f7f7;
    --ink: #6d6d6d;
    --ink-dark: #555555;
    --radius: 18px;
  }
  * { box-sizing: border-box; margin: 0; padding: 0; }
  html, body {
    width: 1200px; height: 900px; overflow: hidden;
    background: var(--bg);
    font-family: "Archivo Narrow", "Arial Narrow", sans-serif;
  }
  .stage { position: relative; width: 1200px; height: 900px; }

  /* Back of card – portrait */
  .card-back {
    position: absolute; left: 150px; top: 170px;
    width: 320px; height: 560px;
    background: var(--paper);
    border-radius: var(--radius);
    overflow: hidden;
  }
  .card-back .logo-band {
    position: absolute; left: 28px; right: 28px; top: 34px; height: 150px;
    background: var(--orange);
    display: flex; flex-direction: column; justify-content: center; align-items: center;
    color: var(--white); font-weight: 600; text-align: center;
  }
  .logo-band .wordmark { font-size: 60px; line-height: 0.95; letter-spacing: 2px; white-space: nowrap; }
  .logo-band .subline { font-size: 19px; letter-spacing: 5px; margin-top: 8px; white-space: nowrap; }

  .card-back .details {
    position: absolute; left: 28px; right: 28px; top: 184px; bottom: 0;
    background: linear-gradient(180deg, var(--white) 0%, var(--orange-soft) 55%, var(--orange) 100%);
  }
  .details .name-band {
    margin-top: 22px; background: var(--orange); color: var(--white);
    padding: 10px 16px; font-size: 26px; font-weight: 700; white-space: nowrap;
  }
  .details .role { padding: 8px 16px 0; font-size: 15px; color: var(--ink); }
  .details .contact { padding: 22px 16px 0; }
  .contact .label { font-size: 13px; font-weight: 700; color: var(--ink-dark); }
  .contact .value { font-size: 14px; color: var(--ink-dark); margin-bottom: 12px; white-space: nowrap; }
  .contact .value.email { font-size: 12px; }
  .details .web {
    position: absolute; left: 16px; right: 16px; bottom: 34px;
    color: var(--white); font-size: 15px; font-weight: 700; white-space: nowrap;
  }

  /* Front of card – landscape */
  .card-front {
    position: absolute; left: 540px; top: 260px;
    width: 560px; height: 340px;
    background: var(--orange);
    border-radius: var(--radius);
    overflow: hidden;
    display: flex; flex-direction: column; justify-content: center; align-items: center;
    color: var(--white); font-weight: 600; text-align: center;
  }
  .card-front .wordmark { font-size: 112px; line-height: 0.9; letter-spacing: 4px; white-space: nowrap; }
  .card-front .subline { font-size: 34px; letter-spacing: 9px; margin-top: 18px; white-space: nowrap; }
</style>
</head>
<body>
  <main class="stage">
    <section class="card-back" aria-label="Back of business card">
      <div class="logo-band">
        <span class="wordmark">VARROW</span>
        <span class="subline">PROPERTY GROUP</span>
      </div>
      <div class="details">
        <div class="name-band">Miles Harcourt</div>
        <p class="role">Managing Director</p>
        <div class="contact">
          <p class="label">telephone</p>
          <p class="value">+61 455 207 364</p>
          <p class="label">email</p>
          <p class="value email">miles.harcourt@varrowgroup-example.com.au</p>
        </div>
        <p class="web">www.varrowgroup-example.com.au</p>
      </div>
    </section>

    <section class="card-front" aria-label="Front of business card">
      <span class="wordmark">VARROW</span>
      <span class="subline">PROPERTY GROUP</span>
    </section>
  </main>
</body>
</html>
```